Content processing platform needs a landing page for products

We need a general landing page for products that we are launching. The concept of the product page is to do two things: a) Get users to sign up for our waitlist (que) so they get access to the product (we give access weekly). b) To generate interest for future products that we have not decided on yet. Mockups: Please see our mockups for inspiration. You have pretty free hands to combine, but please don't let our users think :-). Style: Please use the colours of our style sheet and see the home page (penlyhub.com) for inspiration on how we want the style and tone to be. The final design should communicate "scaling".

Target Market(s)

B2B - online businesses big and small that wish to scale their production of content and translation.

Industry/Entity Type

SaaS

Number of Pages Required

1 page

Font styles to use
Other font styles liked:
• open sans

Requirements
Must have
• Follow our styleguide.

```html
<!DOCTYPE html>
<html lang="en">
<head>
<meta charset="utf-8">
<title>Penlyhub — Products</title>
<link href="https://fonts.googleapis.com/css2?family=Open+Sans:wght@400;600;700&display=swap" rel="stylesheet">
<style>
  :root {
    --page: #1c1c1c;
    --band: #000000;
    --ink-dim: #121212;
    --ink-muted: #2a2a2a;
    --accent-dim: #5a1129;
    --accent-deep: #3d0a17;
    --accent: #ff2f6e;
    --accent-line: #e0306a;
    --modal: #000000;
    --modal-title: #4a4a4a;
    --modal-copy: #5c5c5c;
    --field: #3e3e3e;
    --field-text: #dcdcdc;
    --card: #171717;
    --card-text: #272727;
    --connector: #0b2838;
  }
  * { box-sizing: border-box; margin: 0; padding: 0; }
  html, body { width: 800px; height: 1200px; overflow: hidden; background: var(--page); }
  body { font-family: "Open Sans", sans-serif; position: relative; }

  .backdrop { position: absolute; inset: 0; width: 800px; height: 1200px; }

  .site-nav { position: absolute; top: 22px; left: 0; width: 800px; height: 28px; }
  .brand-name { position: absolute; left: 88px; top: 4px; font-weight: 700; font-size: 14px; color: var(--ink-dim); letter-spacing: .3px; }
  .nav-links { position: absolute; left: 263px; top: 3px; display: flex; gap: 24px; list-style: none; }
  .nav-links li { font-weight: 600; font-size: 14.5px; color: var(--ink-dim); letter-spacing: .3px; }
  .nav-links li.is-active { color: var(--accent-dim); }

  .hero-visual { position: absolute; left: 132px; top: 112px; width: 190px; height: 205px;
    background: linear-gradient(90deg, #050505, #111 60%, #070707); }
  .hero-arrow { position: absolute; top: 220px; width: 14px; height: 18px; }
  .hero-arrow.prev { left: 98px; }
  .hero-arrow.next { left: 690px; }
  .hero-signup { position: absolute; left: 412px; top: 122px; width: 260px; text-align: center; }
  .hero-title { font-weight: 700; font-size: 22px; color: var(--ink-dim); letter-spacing: .6px; }
  .hero-lead { margin-top: 30px; font-size: 11px; color: var(--ink-dim); }
  .hero-lead b { font-weight: 700; }
  .hero-field { margin: 12px auto 0; width: 220px; height: 30px; border: 2px solid var(--accent-dim);
    font-size: 11px; line-height: 26px; color: var(--ink-muted); }
  .hero-button { margin: 14px auto 0; width: 64px; height: 28px; border-radius: 7px; background: var(--accent-dim);
    color: var(--accent-deep); font-weight: 700; font-size: 11.5px; line-height: 28px; }

  .testimonials { position: absolute; top: 804px; left: 0; width: 800px; height: 230px; }
  .testimonial { position: absolute; top: 0; width: 185px; height: 228px; background: var(--card); border-radius: 8px; }
  .testimonial:nth-child(1) { left: 98px; }
  .testimonial:nth-child(2) { left: 304px; }
  .testimonial:nth-child(3) { left: 513px; }
  .testimonial-place { position: absolute; top: 96px; width: 100%; text-align: center; font-size: 7px; color: var(--card-text); }
  .testimonial-quote { position: absolute; top: 124px; left: 14px; right: 4px; font-size: 7.6px; line-height: 10.8px; color: var(--card-text); }
  .connectors { position: absolute; top: 1006px; left: 0; width: 800px; height: 14px; }

  .site-footer { position: absolute; top: 1132px; left: 0; width: 800px; height: 68px; }
  .footer-links { position: absolute; left: 102px; top: 0; list-style: none; }
  .footer-links li { font-size: 6.5px; font-weight: 600; line-height: 17px; color: #151515; }
  .footer-links li.is-active { color: #3a0c1a; }
  .newsletter { position: absolute; left: 516px; top: 16px; }
  .newsletter-label { font-size: 7px; font-weight: 600; color: #151515; letter-spacing: .3px; }
  .newsletter-row { display: flex; gap: 12px; margin-top: 6px; margin-left: 13px; }
  .newsletter-field { width: 105px; height: 16px; background: #0c0c0c; font-size: 6px; line-height: 16px; text-align: center; color: #161616; }
  .newsletter-button { width: 52px; height: 18px; border-radius: 9px; background: #1e0710; color: #3a0c1a; font-size: 7.5px; font-weight: 700; line-height: 18px; text-align: center; }

  .launch-modal { position: absolute; left: 117px; top: 318px; width: 575px; height: 574px; background: var(--modal);
    border-radius: 16px; text-align: center; }
  .launch-badge { position: absolute; top: 44px; width: 100%; font-weight: 700; font-size: 22px; color: var(--modal-title); }
  .launch-visual { position: absolute; left: 219px; top: 122px; width: 192px; height: 216px;
    background: linear-gradient(180deg, #2a2a2a 0%, #181818 60%, #000 100%); }
  .launch-lead { position: absolute; top: 332px; width: 100%; font-size: 23px; color: var(--modal-copy); }
  .launch-lead b { font-weight: 700; }
  .launch-field { position: absolute; left: 149px; top: 396px; width: 275px; height: 36px; background: var(--field);
    border: 2px solid var(--accent-line); color: var(--field-text); font-size: 16px; line-height: 32px; }
  .launch-button { position: absolute; left: 221px; top: 463px; width: 116px; height: 34px; border-radius: 10px;
    background: var(--accent); color: #fff; font-weight: 700; font-size: 18px; line-height: 34px; letter-spacing: .3px; }
</style>
</head>
<body>
  <svg class="backdrop" viewBox="0 0 1000 1500" preserveAspectRatio="none" aria-hidden="true">
    <polygon fill="var(--band)" points="0,145 1000,520 1000,640 0,650"/>
    <polygon fill="var(--band)" points="0,980 1000,1010 1000,1310 520,1500 0,1500"/>
  </svg>

  <header class="site-nav">
    <span class="brand-name">Penlyhub</span>
    <ul class="nav-links">
      <li class="is-active">PRODUCTS</li>
      <li>APPS</li>
      <li>BLOG</li>
      <li>HELP</li>
    </ul>
  </header>

  <section class="hero">
    <div class="hero-visual" role="img" aria-label="Dispenser bottle product next to its box"></div>
    <svg class="hero-arrow prev" viewBox="0 0 14 18" aria-hidden="true"><polyline points="10,2 3,9 10,16" fill="none" stroke="#141414" stroke-width="1.5"/></svg>
    <svg class="hero-arrow next" viewBox="0 0 14 18" aria-hidden="true"><polyline points="4,2 11,9 4,16" fill="none" stroke="#2a2a2a" stroke-width="1.5"/></svg>
    <div class="hero-signup">
      <h1 class="hero-title">SOON AVAILABLE</h1>
      <p class="hero-lead"><b>SIGN UP</b> to be the first in line</p>
      <div class="hero-field">Email</div>
      <div class="hero-button">SIGN UP</div>
    </div>
  </section>

  <section class="testimonials">
    <article class="testimonial">
      <p class="testimonial-place">24, USA</p>
      <p class="testimonial-quote">Lorem ipsum dolor sit amet, consectetur adipiscing elit, sed do eiusmod tempor incididunt ut labore et dolore magna aliqua. Ut enim ad minim veniam, quis nostrud exercitation ullamco laboris nisi ut aliquip ex ea commodo consequat.</p>
    </article>
    <article class="testimonial">
      <p class="testimonial-place">24, USA</p>
      <p class="testimonial-quote">Lorem ipsum dolor sit amet, consectetur adipiscing elit, sed do eiusmod tempor incididunt ut labore et dolore magna aliqua. Ut enim ad minim veniam, quis nostrud exercitation ullamco laboris nisi ut aliquip ex ea commodo consequat.</p>
    </article>
    <article class="testimonial">
      <p class="testimonial-place">24, USA</p>
      <p class="testimonial-quote">Lorem ipsum dolor sit amet, consectetur adipiscing elit, sed do eiusmod tempor incididunt ut labore et dolore magna aliqua. Ut enim ad minim veniam, quis nostrud exercitation ullamco laboris nisi ut aliquip ex ea commodo consequat.</p>
    </article>
  </section>
  <svg class="connectors" viewBox="0 0 800 14" aria-hidden="true">
    <line x1="264" y1="7" x2="314" y2="7" stroke="var(--connector)" stroke-width="1.5"/>
    <circle cx="264" cy="7" r="5" fill="var(--connector)"/>
    <circle cx="314" cy="7" r="5" fill="var(--connector)"/>
    <line x1="480" y1="7" x2="528" y2="7" stroke="var(--connector)" stroke-width="1.5"/>
    <circle cx="480" cy="7" r="5" fill="var(--connector)"/>
    <circle cx="528" cy="7" r="5" fill="var(--connector)"/>
  </svg>

  <footer class="site-footer">
    <ul class="footer-links">
      <li class="is-active">Products</li>
      <li>Quality check</li>
      <li>Reviews</li>
      <li>Help</li>
    </ul>
    <div class="newsletter">
      <p class="newsletter-label">SIGN UP TO OUR NEWSLETTER</p>
      <div class="newsletter-row">
        <div class="newsletter-field">Email</div>
        <div class="newsletter-button">SIGN UP</div>
      </div>
    </div>
  </footer>

  <section class="launch-modal" aria-label="New product sign up">
    <h2 class="launch-badge">NEW!</h2>
    <div class="launch-visual" role="img" aria-label="New dispenser bottle product standing beside its packaging box"></div>
    <p class="launch-lead"><b>SIGN UP</b> to be the first in line</p>
    <div class="launch-field">Email</div>
    <div class="launch-button">SIGN UP</div>
  </section>
</body>
</html>
```